Business Card Design Project

use presentation folder design and my logo and make 4 over 4 business cards

Industry/Entity Type

Business

Requirements
Must have
• use the design from my presentation folder and put my logo on it

Name
Title
phone
fax
email

```html
<!DOCTYPE html>
<html lang="en">
<head>
<meta charset="utf-8">
<title>Ridgeway Counseling – Business Card</title>
<link rel="stylesheet" href="https://fonts.googleapis.com/css2?family=Tinos&family=Questrial&display=swap">
<style>
  :root {
    --page: #fcfcfc;
    --sheet: #ffffff;
    --cream: #f9f6f3;
    --brown: #7a4419;
    --brown-light: #9a5a24;
    --grey-dark: #808080;
    --grey-mid: #a8a8a8;
    --grey-soft: #dedbd9;
    --ink-grey: #777777;
  }
  html, body {
    margin: 0;
    padding: 0;
    width: 1200px;
    height: 1000px;
    overflow: hidden;
    background: var(--page);
  }
  .canvas {
    position: relative;
    width: 1200px;
    height: 1000px;
    overflow: hidden;
  }
  .sheet {
    position: absolute;
    left: 147px;
    top: 0;
    width: 906px;
    height: 1000px;
    background: var(--sheet);
  }
  .card {
    position: absolute;
    left: 227px;
    width: 746px;
    height: 415px;
    background: var(--cream);
    overflow: hidden;
  }
  .card--front { top: 66px; }
  .card--back { top: 519px; }
  .card__art {
    position: absolute;
    inset: 0;
    width: 100%;
    height: 100%;
  }
  .brand {
    position: absolute;
    display: flex;
    align-items: center;
  }
  .brand__dot {
    border-radius: 50%;
    background: var(--grey-mid);
    flex: none;
  }
  .brand__name {
    font-family: "Tinos", "Times New Roman", serif;
    color: var(--brown);
    white-space: nowrap;
  }
  .brand--front {
    left: 140px;
    top: 175px;
    gap: 18px;
  }
  .brand--front .brand__dot { width: 54px; height: 54px; }
  .brand--front .brand__name { font-size: 50px; }

  .person {
    position: absolute;
    left: 110px;
    top: 108px;
    margin: 0;
    font-family: "Tinos", "Times New Roman", serif;
    font-weight: 400;
    font-size: 56px;
    line-height: 1;
    color: var(--ink-grey);
    white-space: nowrap;
  }
  .person__surname { color: var(--brown); }
  .job-title {
    position: absolute;
    left: 312px;
    top: 186px;
    margin: 0;
    font-family: "Questrial", "Helvetica", sans-serif;
    font-size: 38px;
    line-height: 1;
    color: var(--brown);
    white-space: nowrap;
  }
  .brand--back {
    right: 304px;
    top: 338px;
    gap: 6px;
  }
  .brand--back .brand__dot { width: 15px; height: 15px; }
  .brand--back .brand__name { font-size: 15px; }
  .divider {
    position: absolute;
    left: 457px;
    top: 314px;
    width: 1.5px;
    height: 68px;
    background: var(--brown);
  }
  .contact {
    position: absolute;
    left: 473px;
    top: 313px;
    margin: 0;
    padding: 0;
    list-style: none;
    font-family: "Questrial", "Helvetica", sans-serif;
    font-size: 18.5px;
    line-height: 25px;
    color: var(--brown);
    white-space: nowrap;
  }
</style>
</head>
<body>
<div class="canvas">
  <div class="sheet"></div>

  <section class="card card--front" aria-label="Card front">
    <svg class="card__art" viewBox="0 0 746 415" preserveAspectRatio="none" aria-hidden="true">
      <defs>
        <linearGradient id="brownWash" x1="0" y1="0" x2="1" y2="1">
          <stop offset="0" stop-color="#a0693a"/>
          <stop offset="0.3" stop-color="#8c5120"/>
          <stop offset="1" stop-color="#8a4f1c"/>
        </linearGradient>
        <linearGradient id="greyWash" x1="0" y1="0" x2="1" y2="1">
          <stop offset="0" stop-color="#8a8a8a"/>
          <stop offset="0.5" stop-color="#b3b3b3"/>
          <stop offset="1" stop-color="#8e8e8e"/>
        </linearGradient>
      </defs>
      <path d="M0 0 H340 C300 60 220 85 120 108 C40 128 25 200 40 255 C65 330 135 380 180 415 H0 Z" fill="url(#brownWash)"/>
      <path d="M265 100 C360 45 500 -10 600 22 C690 55 700 150 662 250 C632 322 605 380 592 415 H746 V0 H375 C330 35 295 75 265 100 Z" fill="url(#greyWash)"/>
    </svg>
    <div class="brand brand--front">
      <span class="brand__dot"></span>
      <span class="brand__name">Ridgeway Counseling</span>
    </div>
  </section>

  <section class="card card--back" aria-label="Card back">
    <svg class="card__art" viewBox="0 0 746 415" preserveAspectRatio="none" aria-hidden="true">
      <defs>
        <linearGradient id="greyLeft" x1="0" y1="0" x2="0" y2="1">
          <stop offset="0" stop-color="#8e8e8e"/>
          <stop offset="1" stop-color="#a9a9a9"/>
        </linearGradient>
      </defs>
      <path d="M0 0 H38 C12 80 18 200 58 300 C95 375 140 410 165 415 H0 Z" fill="url(#greyLeft)"/>
      <path d="M38 0 H130 C82 60 68 150 78 250 C88 330 138 390 168 415 H165 C125 385 78 325 50 245 C25 165 18 75 38 0 Z" fill="var(--grey-soft)"/>
      <path d="M365 0 H548 C622 42 690 122 730 222 C668 158 578 102 470 60 C420 40 382 20 365 0 Z" fill="var(--brown)"/>
      <path d="M702 0 H746 V222 C722 180 702 122 692 50 Z" fill="var(--grey-dark)"/>
    </svg>
    <h1 class="person">Name <span class="person__surname">Surname</span></h1>
    <p class="job-title">Job Title</p>
    <div class="brand brand--back">
      <span class="brand__dot"></span>
      <span class="brand__name">Ridgeway Counseling</span>
    </div>
    <span class="divider"></span>
    <ul class="contact">
      <li>Phone:</li>
      <li>Fax:</li>
      <li>xxx.xxx.xxx@ridgeway.com</li>
    </ul>
  </section>
</div>
</body>
</html>
```